Floral Waters needs a Label Design for bottles

Our products slogan: grown with water and sun.
Organic products of excellence originating from regions of extraordinary environmental quality, these products are the basis of natural cosmetics. Bio certificated and Organic.

We need a Luxury Label for the bottles of Floral Waters.
We don't want rustic, organic, rural, bio...
We want Luxury associated with environment.

The Label / decoration for the bottles must be editable, for we can change the titles of the floral Waters and information.
Elements :
Floral Water
Pet and Glass round Bottles Dimensions: 11cm Height , 4.5cm width
perimeter - 7.65
The logo is from tv lumora web store, it´s not necessary to include in the front of the paching design. it´s an open option

Target Market(s)

Medium High urban people , with ecologic and sustainable concerns. People who prefer natural and non Quimical cosmetics.

Industry/Entity Type

Floral

Requirements
Must have
• Sophisticated simple design
• Elements :
• Floral Water
• space for the name of the Floral Water ( ex: Salvia Officinalis, Minth, Melissa Officinalis)
• Grown with water and sun
Nice to have
• Variations of Gold
Should not have
• Bio, farm, organic, rustic,

```html
<!DOCTYPE html>
<html lang="en">
<head>
<meta charset="utf-8">
<title>Floral Water Labels</title>
<link rel="stylesheet" href="https://fonts.googleapis.com/css2?family=Great+Vibes&family=PT+Sans:wght@400&display=swap">
<style>
  :root {
    --page: #ffffff;
    --sage: #9a8cc6;
    --melissa: #7b9c39;
    --mint: #21b47e;
    --gold: #e6d46a;
    --gold-deep: #b99a2e;
    --text-light: #ffffff;
    --mark: #2e7a3a;
  }
  * { margin: 0; padding: 0; box-sizing: border-box; }
  html, body {
    width: 1200px;
    height: 1033px;
    overflow: hidden;
    background: var(--page);
  }
  .label-set {
    position: relative;
    width: 1200px;
    height: 1033px;
  }
  .label {
    position: absolute;
    top: 348px;
    width: 242px;
    height: 576px;
    overflow: hidden;
    font-family: "PT Sans", sans-serif;
    color: var(--text-light);
  }
  .label--sage { left: 144px; background: var(--sage); }
  .label--melissa { left: 470px; background: var(--melissa); }
  .label--mint { left: 792px; background: var(--mint); }

  .ornament {
    position: absolute;
    background: linear-gradient(135deg, var(--gold) 0%, var(--gold-deep) 100%);
    opacity: 0.55;
  }
  .ornament--top {
    left: 8px;
    top: 0;
    width: 200px;
    height: 168px;
    border-radius: 0 0 100% 0 / 0 0 70% 30%;
  }
  .ornament--bottom {
    right: 6px;
    bottom: 0;
    width: 200px;
    height: 176px;
    border-radius: 100% 0 0 0 / 40% 0 0 0;
  }

  .slogan {
    position: absolute;
    top: 124px;
    right: 18px;
    width: 150px;
    text-align: center;
    font-size: 19px;
    line-height: 26px;
  }
  .product-name {
    position: absolute;
    top: 268px;
    left: 0;
    width: 100%;
    text-align: center;
    font-family: "Great Vibes", cursive;
    font-size: 27px;
    line-height: 34px;
    color: var(--gold);
    white-space: nowrap;
  }
  .product-name--short { font-size: 40px; top: 258px; }
  .product-type {
    position: absolute;
    top: 304px;
    left: 0;
    width: 100%;
    text-align: center;
    font-size: 25px;
    letter-spacing: 0.5px;
  }
  .brand {
    position: absolute;
    top: 422px;
    left: 50%;
    transform: translateX(-50%);
    width: 60px;
    height: 60px;
    background: #ffffff;
    display: flex;
    align-items: center;
    justify-content: center;
    text-align: center;
    font-family: "PT Sans", sans-serif;
    font-size: 11px;
    line-height: 12px;
    color: var(--mark);
  }
</style>
</head>
<body>
<main class="label-set">

  <section class="label label--sage">
    <div class="ornament ornament--top" role="img" aria-label="Gold floral flourish ornament in the upper corner"></div>
    <p class="slogan">Grown with water and sun</p>
    <h2 class="product-name">Salvia Officinalis</h2>
    <p class="product-type">FLORAL WATER</p>
    <div class="brand">tv lumora</div>
    <div class="ornament ornament--bottom" role="img" aria-label="Gold floral flourish ornament in the lower corner"></div>
  </section>

  <section class="label label--melissa">
    <div class="ornament ornament--top" role="img" aria-label="Gold floral flourish ornament in the upper corner"></div>
    <p class="slogan">Grown with water and sun</p>
    <h2 class="product-name">Melissa Officinalis</h2>
    <p class="product-type">FLORAL WATER</p>
    <div class="brand">tv lumora</div>
    <div class="ornament ornament--bottom" role="img" aria-label="Gold floral flourish ornament in the lower corner"></div>
  </section>

  <section class="label label--mint">
    <div class="ornament ornament--top" role="img" aria-label="Gold floral flourish ornament in the upper corner"></div>
    <p class="slogan">Grown with water and sun</p>
    <h2 class="product-name product-name--short">Minth</h2>
    <p class="product-type">FLORAL WATER</p>
    <div class="brand">tv lumora</div>
    <div class="ornament ornament--bottom" role="img" aria-label="Gold floral flourish ornament in the lower corner"></div>
  </section>

</main>
</body>
</html>
```